Lifecoach needs website design based on a standard Wordpress theme

I need a website for my new lifecoaching business that can be easily implemented in Wordpress, it needs to be compatible with a standard Wordpress theme. So I can place the pictures, texts etc. in a standard theme of Wordpress.

I want the design to be a very good feeling and playfull one, based on my logo.

Target Market(s)

I will coach people to reach their goals and dreams in life.

Industry/Entity Type

Business

Requirements
Must have
• Can be easy implemented in Wordpress.
Nice to have
• Photo's of nature are nice.

```html
<!DOCTYPE html>
<html lang="en">
<head>
<meta charset="utf-8">
<title>Anna Bloemhof Lifecoach</title>
<link href="https://fonts.googleapis.com/css2?family=Open+Sans:wght@400;600&display=swap" rel="stylesheet">
<style>
:root{
  --navy:#005282;
  --sky:#12a6e3;
  --sky-deep:#0a8fd0;
  --leaf:#6cba38;
  --leaf-light:#9fd458;
  --text:#555;
  --white:#fff;
}
*{box-sizing:border-box;margin:0;padding:0}
html,body{width:960px;height:1200px;overflow:hidden}
body{font-family:'Open Sans',sans-serif;color:var(--text);background:var(--white);position:relative}
.wrap{position:absolute;left:104px;width:752px}
.header{position:absolute;top:0;left:0;width:960px;height:80px;background:var(--white)}
.brand{position:absolute;left:104px;top:18px;display:flex;align-items:center;gap:8px}
.brand-mark{width:46px;height:46px;border-radius:50%;background:var(--sky)}
.brand-name{font-size:16px;font-weight:600;color:var(--navy);line-height:1.1}
.follow{position:absolute;right:104px;top:14px;display:flex;align-items:center;gap:7px;font-size:11.5px;font-weight:600;color:var(--navy)}
.follow span{margin-right:4px}
.social{width:18px;height:18px;border-radius:3px;background:var(--sky)}
.call{position:absolute;right:104px;top:46px;width:192px;height:34px;background:var(--sky);color:var(--white);font-size:15px;display:flex;align-items:center;gap:6px;padding-left:10px}
.nav-band{position:absolute;top:80px;left:0;width:960px;height:63px;background:var(--navy)}
.page-bg{position:absolute;top:143px;left:0;width:960px;height:971px;background:linear-gradient(#ececec,#fff 260px)}
.nav{top:95px;display:flex;justify-content:space-between;font-size:9.5px;font-weight:600;color:var(--white);letter-spacing:.3px}
.slider{top:122px;height:320px;background:var(--white);padding:4px;box-shadow:0 1px 3px rgba(0,0,0,.3)}
.slide{position:relative;width:100%;height:100%;background:linear-gradient(180deg,var(--leaf) 0%,var(--leaf-light) 100%)}
.slide h1{position:absolute;left:35px;top:104px;width:540px;font-size:26px;font-weight:600;line-height:32px;color:var(--white);text-shadow:0 1px 3px rgba(0,0,0,.35)}
.dots{position:absolute;left:35px;top:285px;display:flex;gap:6px}
.dots i{width:13px;height:13px;border-radius:50%;background:var(--white)}
.dots i.on{background:var(--navy)}
.cards{top:470px;display:flex;justify-content:space-between}
.card{width:240px;height:261px;background:var(--navy);color:var(--white);padding:16px 19px;position:relative}
.card h2{font-size:17px;font-weight:600;margin-bottom:12px}
.card p{font-size:10.5px;line-height:18.4px}
.ticks{list-style:none;font-size:10.5px}
.ticks li{display:flex;align-items:center;gap:9px;height:22.4px}
.btn{position:absolute;left:19px;bottom:14px;width:94px;height:29px;background:var(--sky);color:var(--white);font-size:10.5px;letter-spacing:1px;display:flex;align-items:center;justify-content:center}
.news{display:flex;gap:12px;padding-bottom:10px;margin-bottom:10px;border-bottom:1px solid rgba(255,255,255,.3)}
.news:last-of-type{border:0}
.date{width:43px;height:50px;flex:none;background:var(--sky-deep);text-align:center;line-height:1}
.date b{display:block;font-weight:400;font-size:13px;padding-top:6px}
.date em{display:block;font-style:normal;font-size:25px;padding-top:2px}
.news p{font-size:10.5px;line-height:16px}
.testi-title{top:760px;text-align:center;font-size:17px;font-weight:600;color:var(--navy)}
.quote{top:795px;text-align:center;font-size:10.5px;line-height:18.4px;padding:0 34px}
.qmark{position:absolute;top:0;font-size:30px;font-weight:600;color:var(--sky);line-height:1}
.avatar{position:absolute;left:446px;top:860px;width:68px;height:68px;border-radius:50%;background:linear-gradient(#e3e6ea,#aeb6c0);border:3px solid #ddd}
.person{top:930px;text-align:center;line-height:15px}
.person b{display:block;font-weight:600;font-size:12.5px;color:var(--sky)}
.person span{font-size:10.5px}
.divider{top:977px;height:1px;background:#ddd}
.partners-title{top:998px;text-align:center;font-size:17px;font-weight:600;color:var(--navy)}
.partners{top:1040px;height:40px;display:flex;align-items:center;justify-content:space-between;padding:0 16px}
.arrow{width:22px;height:22px;border-radius:50%;background:#ccc;display:flex;align-items:center;justify-content:center}
.badge{width:100px;height:30px;border-radius:4px;background:#d6dce2}
.footer{position:absolute;top:1114px;left:0;width:960px;height:86px;background:var(--navy);color:var(--white);text-align:center;font-size:10px;line-height:16px;padding-top:20px}
.footer a{color:var(--sky);text-decoration:none}
</style>
</head>
<body>
<header class="header">
  <div class="brand"><div class="brand-mark"></div><div class="brand-name">Anna Bloemhof<br>Lifecoach</div></div>
  <div class="follow"><span>Follow Us:</span><i class="social"></i><i class="social"></i><i class="social"></i><i class="social"></i></div>
  <div class="call">
    <svg width="16" height="16" viewBox="0 0 16 16"><rect width="16" height="16" rx="3" fill="#fff"/><path d="M5 3l2 2-1 1.5c.6 1.4 1.6 2.4 3 3L10.5 8.5l2 2-1.5 1.8C7 12 4 9 3.7 4.6z" fill="#12a6e3"/></svg>
    Call Us: 555 010 2468
  </div>
</header>
<div class="nav-band"></div>
<div class="page-bg"></div>
<nav class="wrap nav"><span>HOME</span><span>WHO WE ARE</span><span>WHAT WE DO</span><span>LATEST NEWS</span><span>TESTIMONIALS</span><span>BLOG</span><span>CONTACT US</span></nav>

<section class="wrap slider">
  <div class="slide" role="img" aria-label="Nature photo of fresh green leaves growing beside a tree trunk">
    <h1>We specialize in transition life coaching for personal and professional empowerment..</h1>
    <div class="dots"><i class="on"></i><i></i><i></i><i></i></div>
  </div>
</section>

<section class="wrap cards">
  <article class="card">
    <h2>WHO WE ARE</h2>
    <p>Aliquam molestie, mi et imperdiet euismod, dui purus auctor tellus, et interdum lacus lectus et ante. Sed accumsan sollicitudin sapien, sit amet adipiscing turpis gravida ac. In congue, neque ac lobortis volutpat, libero mauris varius mi, vitae suscipit ipsum ligula vitae risus.</p>
    <span class="btn">READ MORE</span>
  </article>
  <article class="card">
    <h2>WHAT WE DO</h2>
    <ul class="ticks">
      <li><svg width="11" height="10" viewBox="0 0 11 10"><path d="M1 5l3 3 6-7" stroke="#12a6e3" stroke-width="2.4" fill="none"/></svg>Aliquam molestie mi et imperdiet</li>
      <li><svg width="11" height="10" viewBox="0 0 11 10"><path d="M1 5l3 3 6-7" stroke="#12a6e3" stroke-width="2.4" fill="none"/></svg>Dui purus auctor tellus</li>
      <li><svg width="11" height="10" viewBox="0 0 11 10"><path d="M1 5l3 3 6-7" stroke="#12a6e3" stroke-width="2.4" fill="none"/></svg>Interdum lacus lectus et ante</li>
      <li><svg width="11" height="10" viewBox="0 0 11 10"><path d="M1 5l3 3 6-7" stroke="#12a6e3" stroke-width="2.4" fill="none"/></svg>Sed accumsan sollicitudin sapien</li>
      <li><svg width="11" height="10" viewBox="0 0 11 10"><path d="M1 5l3 3 6-7" stroke="#12a6e3" stroke-width="2.4" fill="none"/></svg>Sit amet adipiscing turpis gravida ac</li>
      <li><svg width="11" height="10" viewBox="0 0 11 10"><path d="M1 5l3 3 6-7" stroke="#12a6e3" stroke-width="2.4" fill="none"/></svg>In congue neque ac lobortis</li>
      <li><svg width="11" height="10" viewBox="0 0 11 10"><path d="M1 5l3 3 6-7" stroke="#12a6e3" stroke-width="2.4" fill="none"/></svg>Vitae suscipit ipsum</li>
    </ul>
    <span class="btn">READ MORE</span>
  </article>
  <article class="card">
    <h2>LATEST NEWS</h2>
    <div class="news"><div class="date"><b>Apr</b><em>07</em></div><p>Aliquam molestie, mi et imperdiet euismod, dui purus auctor tellus, et interdum lacus lectus et ante....</p></div>
    <div class="news"><div class="date"><b>Apr</b><em>07</em></div><p>Aliquam molestie, mi et imperdiet euismod, dui purus auctor tellus, et interdum lacus lectus et ante....</p></div>
    <span class="btn">READ ALL</span>
  </article>
</section>

<h2 class="wrap testi-title">TESTIMONIALS</h2>
<blockquote class="wrap quote">
  <span class="qmark" style="left:0">&ldquo;</span>
  Ut et scelerisque ante. Donec erat purus, faucibus vitae congue vel, porttitor nec lectus. Aenean a nibh eget turpis vehicula tempus ac sed massa. Vestibulum dolor nulla, ultrices ac tincidunt sed, laoreet non est. Suspendisse lobortis turpis in odio blandit ac interdum lorem euismod. Etiam risus massa, vulputate eu pellentesque et, consectetur a neque.
  <span class="qmark" style="right:0">&rdquo;</span>
</blockquote>
<div class="avatar" role="img" aria-label="Portrait photo of the client giving the testimonial"></div>
<div class="wrap person"><b>Daniel Reyes</b><span>Location goes here</span></div>
<div class="wrap divider"></div>

<h2 class="wrap partners-title">Our Partners</h2>
<div class="wrap partners">
  <span class="arrow"><svg width="8" height="10" viewBox="0 0 8 10"><path d="M6 1L2 5l4 4" stroke="#fff" stroke-width="2" fill="none"/></svg></span>
  <i class="badge"></i><i class="badge"></i><i class="badge"></i><i class="badge" style="width:150px"></i>
  <span class="arrow"><svg width="8" height="10" viewBox="0 0 8 10"><path d="M2 1l4 4-4 4" stroke="#fff" stroke-width="2" fill="none"/></svg></span>
</div>

<footer class="footer">Copyright © 2014.<a href="#">Anna Bloemhof Life Coach</a><br>All Right Reserved</footer>
</body>
</html>
```